The Drifters

Copper Heron Productions is looking for their theatrical poster for their film 'THE DRIFTERS'... It is a zombie appocalypse action film made in NSW Australia. See their facebook page www.pagebook.example/THEDRIFTERSFILM...
Updates
Project Deadline Extended
Reason: i have decided to EXTEND the deadline for 5 more days, as there are some really talented artists reviewing their submissions for us... Thank you to all...
Please review the new uploaded images you may or may not want to use to revierw your submissions
Logo Text
Copper Heron Productions
Look and feel
Each slider illustrates characteristics of the customer's brand and the style your logo design should communicate.

```html
<!DOCTYPE html>
<html lang="en">
<head>
<meta charset="utf-8">
<title>The Drifters – Theatrical Poster</title>
<link rel="stylesheet" href="https://fonts.googleapis.com/css2?family=Big+Shoulders+Stencil+Display:wght@800;900&family=Russo+One&family=Bebas+Neue&display=swap">
<style>
  :root {
    --page: #ffffff;
    --concrete-light: #a3a6a4;
    --concrete-mid: #858987;
    --concrete-dark: #5d625f;
    --ink-light: #e4e4e2;
    --ink-shadow: #1c1c1c;
    --steel-band: rgba(70, 74, 72, 0.78);
    --steel-edge: #2e3231;
    --silver-top: #ffffff;
    --silver-bottom: #9a9c9c;
    --blood: #b0121a;
    --credit-ink: #f2f2f0;
    --badge: #ffffff;
    --badge-edge: #111111;
  }
  * { margin: 0; padding: 0; box-sizing: border-box; }
  html, body {
    width: 922px; height: 1200px; overflow: hidden;
    background: var(--page);
  }
  .poster {
    position: absolute; left: 50px; top: 10px;
    width: 822px; height: 1180px;
    background:
      radial-gradient(ellipse at 30% 60%, var(--concrete-dark) 0%, transparent 45%),
      radial-gradient(ellipse at 75% 25%, var(--concrete-light) 0%, transparent 50%),
      linear-gradient(180deg, var(--concrete-mid), var(--concrete-light) 55%, var(--concrete-mid));
    overflow: hidden;
  }
  .studio-line, .tagline {
    position: absolute; left: 0; width: 100%; text-align: center;
    font-family: "Big Shoulders Stencil Display", sans-serif;
    font-weight: 900;
    color: var(--ink-light);
    text-shadow: 2px 2px 3px var(--ink-shadow);
    white-space: nowrap;
    line-height: 1;
  }
  .studio-line { letter-spacing: 2px; }
  .studio-line--presents { top: 14px; font-size: 32px; }
  .studio-line--film { top: 48px; font-size: 30px; }
  .hazard-emblem {
    position: absolute; left: 24px; top: 122px;
    width: 790px; height: 700px;
  }
  .title-band {
    position: absolute; left: 0; top: 420px;
    width: 100%; height: 166px;
    background: var(--steel-band);
    border-top: 2px solid var(--steel-edge);
    border-bottom: 2px solid var(--steel-edge);
  }
  .title {
    position: absolute; left: 0; width: 100%; text-align: center;
    font-family: "Russo One", sans-serif;
    font-weight: 400;
    line-height: 1;
    white-space: nowrap;
    background: linear-gradient(180deg, var(--silver-top), var(--silver-bottom));
    -webkit-background-clip: text; background-clip: text;
    color: transparent;
    filter: drop-shadow(3px 3px 0 var(--blood)) drop-shadow(2px 3px 3px var(--ink-shadow));
  }
  .title--article { top: 350px; font-size: 60px; letter-spacing: 3px; }
  .title--main { top: 454px; font-size: 128px; letter-spacing: 4px; }
  .tagline { font-size: 31px; letter-spacing: 2px; }
  .tagline--first { top: 708px; }
  .tagline--second { top: 762px; }
  .credits {
    position: absolute; left: 0; top: 935px; width: 100%;
    font-family: "Bebas Neue", sans-serif;
    font-size: 17px; line-height: 33px;
    color: var(--credit-ink);
    text-align: center; letter-spacing: 0.3px;
  }
  .credits-line { display: block; white-space: nowrap; }
  .credits small { font-size: 10px; letter-spacing: 0; }
  .credits .location { font-size: 14px; }
  .rating-badge {
    position: absolute; left: 340px; top: 1120px;
    width: 138px; height: 34px;
    background: var(--badge); border: 2px solid var(--badge-edge);
  }
</style>
</head>
<body>
  <main class="poster">
    <p class="studio-line studio-line--presents">COPPER HERON PRODUCTIONS PRESENTS</p>
    <p class="studio-line studio-line--film">A DORIAN KELL FILM</p>

    <svg class="hazard-emblem" viewBox="0 0 790 700" role="img" aria-label="Large rust-red and toxic-green hazard emblem behind the title">
      <defs>
        <radialGradient id="rustGlow" cx="50%" cy="50%" r="50%">
          <stop offset="0%" stop-color="#8a3a14"/>
          <stop offset="70%" stop-color="#6e2010"/>
          <stop offset="100%" stop-color="#4a8f1a"/>
        </radialGradient>
      </defs>
      <ellipse cx="395" cy="370" rx="330" ry="320" fill="url(#rustGlow)" opacity="0.55"/>
    </svg>

    <div class="title-band"></div>
    <h1 class="title title--article">THE</h1>
    <h1 class="title title--main">DRIFTERS</h1>

    <p class="tagline tagline--first">BEFORE THEY CAN CURE IT, THEY HAVE TO SURVIVE</p>
    <p class="tagline tagline--second">AND SURVIVING IS SIMPLE... KILL OR BE KILLED</p>

    <p class="credits">
      <span class="credits-line"><small>A</small> COPPER HERON PRODUCTIONS <small>AND</small> DORIAN KELL <small>PRODUCTION</small> "THE DRIFTERS" DORIAN KELL LUCA FERRANTE TESSA MARLOWE OWEN</span>
      <span class="credits-line">STERLING PRIYA VANCE <small>WRITTEN BY</small> DORIAN KELL <small>AND</small> MAREN KELL <small>DIRECTED BY</small> DORIAN KELL <small>EXECUTIVE PRODUCER</small> DORIAN KELL <small>ASSOCIATE PRODUCER</small></span>
      <span class="credits-line">IVY HOLLISTER <small>FILM EDITOR</small> FELIX DRAPER <small>MAKEUP BY</small> HANNAH CORWIN ZARA WHITLOCK CHLOE ASHDOWN MIRANDA THISTLEWOOD <small>SOUND</small></span>
      <span class="credits-line"><small>BY</small> NORA QUILL <small>MUSIC BY</small> REID HARTLEY <small>AND</small> NO SECOND ACT ONLY ANOTHER OPENING <small>SPECIAL FX</small> FELIX DRAPER</span>
      <span class="credits-line location"><small>FILMED ON LOCATION IN</small> BELLMORE RIDGE, NSW, AUSTRALIA</span>
    </p>

    <div class="rating-badge" aria-hidden="true"></div>
  </main>
</body>
</html>
```